8 Page A6 booklet for Hypnosis/Hypnotherapy product

Please see PDF document attached for design brief. The booklet will be printed in http://www.pellavorn.co.uk/shop/brochures

If you do have any further questions please let me know.

This is going to be the insert for my DVD. The graphic for the DVD have now been attached to this project

Target Market(s)

People that have just purchased my Hypnosis CD

Industry/Entity Type

Hypnotherapy

Requirements
Must have
• I have attached a brief. Hopefully this explains but please do let me know if you have any further questions

```html
<!DOCTYPE html>
<html lang="en">
<head>
<meta charset="utf-8">
<title>Hypnosis Session – A6 Booklet</title>
<link rel="stylesheet" href="https://fonts.googleapis.com/css2?family=Montserrat:wght@600;700&family=Mulish:wght@300;400;600;800&display=swap">
<style>
:root{
  --navy:#1c2366;
  --band:#1f64b5;
  --royal:#1d4fa0;
  --sky:#3f8fd6;
  --lavender:#c4c8ea;
  --lilac:#dfe0f3;
  --ink:#141a33;
  --muted:#3c4466;
  --paper:#f1f1f4;
  --white:#ffffff;
}
*{box-sizing:border-box;margin:0;padding:0}
html,body{width:883px;height:1200px;overflow:hidden;background:var(--white)}
body{position:relative;font-family:"Mulish",Arial,sans-serif;color:var(--ink)}

.page{position:absolute;width:250px;height:352px;overflow:hidden;background:var(--paper)}
.page .top{position:absolute;left:0;top:0;width:100%;height:21px;background:var(--navy)}
.page .band{position:absolute;left:0;top:21px;width:100%;height:20px;background:linear-gradient(90deg,var(--royal),var(--band) 60%,var(--sky))}
.running{position:absolute;top:7px;font-size:6.5px;letter-spacing:.2px;color:#cfd5f2}
.running.left{left:17px}
.running.right{right:17px}
.folio{position:absolute;bottom:8px;font-size:7px;color:var(--muted)}
.folio.left{left:14px}.folio.right{right:14px}

.h{font-family:"Montserrat",Arial,sans-serif;font-weight:700;color:var(--navy);font-size:13.5px;letter-spacing:-.2px}
.sub{font-size:10px;color:var(--ink);line-height:1.15}
.small{font-size:6.6px;line-height:1.32;color:var(--ink)}
.abs{position:absolute}

.lilac-bg{background:linear-gradient(160deg,#aab0de 0%,var(--lavender) 40%,var(--lilac) 75%,#eef0fa 100%)}
.wave{position:absolute;top:41px;right:0;height:311px;width:70px}

/* brand wordmark */
.brand{text-align:center;font-family:"Mulish",Arial,sans-serif;font-weight:400;color:var(--royal);letter-spacing:.3px}
.brand .dot{display:inline-block;width:9px;height:9px;border-radius:50%;background:var(--royal);margin-bottom:4px}
.brand .name{display:block;font-size:16px;line-height:1.05}
.brand .line2{display:block;font-size:16px;line-height:1.05}
.url{font-family:"Mulish",Arial,sans-serif;font-weight:600;font-size:8.5px;letter-spacing:.4px;color:var(--navy)}

/* cover */
.cover{left:37px;top:34px;background:radial-gradient(circle at 20% 75%,#e9f0fb 0,#b9cdee 25%,#7fa7dd 55%,#5f8ed0 100%)}
.cover .photo{position:absolute;left:0;top:41px;width:250px;height:200px;background:linear-gradient(120deg,#7da94a 0%,#9bc25c 30%,#d9b49a 55%,#c79a7e 75%,#8fb85a 100%)}
.cover .curve{position:absolute;left:0;top:190px;width:250px;height:70px}
.offer{position:absolute;left:174px;top:166px;width:62px;height:62px;border-radius:50%;background:rgba(255,255,255,.9);text-align:center;padding-top:9px;font-size:8px;line-height:1.05;color:var(--navy)}
.offer b{font-weight:800}
.cover .brand{position:absolute;left:0;width:100%;top:262px}
.cover .url{position:absolute;width:100%;text-align:center;top:327px}

/* spread 1 */
.p2{left:350px;top:35px}
.p3{left:600px;top:35px;background:var(--paper)}
.list-label{font-family:"Montserrat",Arial,sans-serif;font-weight:600;font-size:10px}
.cabin{position:absolute;left:0;top:229px;width:250px;height:123px;background:linear-gradient(180deg,#c9cfdb 0%,#9aa6bb 45%,#5d6b86 100%)}
.partner{font-size:6.6px;line-height:1.25;color:var(--band);text-align:center}

/* spread 2 */
.p4{left:189px;top:414px}
.p5{left:439px;top:414px;background:linear-gradient(90deg,#dcdce2,#fafafa 20%,#ffffff)}
.portrait{position:absolute;left:17px;top:70px;width:103px;height:122px;border-radius:8px;background:linear-gradient(180deg,#f4f5f8 0%,#e3d2c4 45%,#6a5a52 100%)}
.badge{position:absolute;top:255px;height:63px;border-radius:9px;background:var(--white);box-shadow:0 0 0 1px rgba(28,35,102,.08)}
.badge .fill{position:absolute;inset:7px;border-radius:6px}

/* spread 3 */
.p6{left:36px;top:806px;background:linear-gradient(90deg,#f6f6f8,#e7e7ec 90%,#cfd0d8)}
.p7{left:286px;top:806px;background:radial-gradient(circle at 40% 70%,#3b5fbd 0%,#26418f 45%,#1b2c6d 100%)}
.faq-q{font-size:10px;line-height:1.1;margin-top:2px}
.faq-a{font-size:6.5px;line-height:1.3;padding-left:24px}
.deal{position:absolute;left:131px;top:36px;width:96px;height:96px;border-radius:50%;background:radial-gradient(circle at 45% 40%,#f4f5fb,#c8cce6);text-align:center;padding-top:26px;color:var(--navy);font-family:"Montserrat",Arial,sans-serif;font-weight:700;font-size:11.5px;line-height:1.15}
.deal .big{font-size:14px}
.p7 .brand{color:#dfe4fb}
.p7 .brand .dot{background:#dfe4fb}
.p7 .url{color:#eef1ff}

/* back */
.back{left:598px;top:801px;background:radial-gradient(circle at 30% 80%,#dbe8f8 0,#a5c3ec 30%,#6c9ddb 60%,#4c84cc 100%)}
.back .brand{position:absolute;left:0;width:100%;top:80px}
.back .url{position:absolute;width:100%;text-align:center;top:174px}
.back .photo{position:absolute;left:128px;top:218px;width:122px;height:134px;background:linear-gradient(180deg,#d6c1b0 0%,#b18e78 45%,#2f3a52 75%,#1f2740 100%);border-radius:60px 60px 0 0}
</style>
</head>
<body>

<!-- Front cover -->
<section class="page cover">
  <div class="top"></div><div class="band"></div>
  <span class="running right" style="top:29px;font-size:7.5px;color:#fff">HYPNOSIS SESSION</span>
  <div class="photo" role="img" aria-label="Photo of a relaxed woman with closed eyes wearing headphones, green foliage behind"></div>
  <svg class="curve" viewBox="0 0 250 70" preserveAspectRatio="none"><path d="M0 40 C60 10 140 70 250 20 L250 70 L0 70Z" fill="#c9daf3"/></svg>
  <div class="offer">SEE<br>PAGE 7<br><b>exclusive<br>special<br>offer</b></div>
  <div class="brand"><span class="dot"></span><span class="name">LUKE HARWOOD</span><span class="line2">HYPNOTHERAPY</span></div>
  <div class="url">LukeHarwoodHypnotherapy.com</div>
</section>

<!-- Spread: pages 2–3 -->
<section class="page p2 lilac-bg">
  <div class="top"></div><div class="band"></div>
  <span class="running left">HYPNOSIS SESSION</span>
  <svg class="wave" viewBox="0 0 70 311" preserveAspectRatio="none"><path d="M70 0 L35 0 C10 60 60 100 40 160 C20 220 55 260 40 311 L70 311Z" fill="#f1f1f4"/></svg>
  <div class="abs h" style="left:17px;top:72px">CONTENTS</div>
  <div class="abs list-label" style="left:17px;top:95px">CD</div>
  <div class="abs" style="left:47px;top:95px;width:150px">
    <div class="sub">Track 1:<br>Daytime Recording</div>
    <div class="small" style="font-size:6.4px">Use this track when you want<br>to awaken feeling energised</div>
    <div class="sub" style="margin-top:5px">Track 2:<br>Bedtime Recording</div>
    <div class="small" style="font-size:6.4px">Use this track when you wish to<br>drift off to sleep after listening</div>
  </div>
  <div class="abs list-label" style="left:17px;top:190px">Computer Disk</div>
  <div class="abs" style="left:47px;top:204px;width:170px">
    <div class="sub">Video:</div>
    <div class="small">Introduction to your recordings and<br>some added techniques that you can use</div>
    <div class="sub">PDF:</div>
    <div class="small">Reference document of things that you<br>can do to accelerate your progress</div>
    <div class="sub">MP3 versions:</div>
    <div class="small">These are the 2 CD tracks in MP3 format<br>so that they are ready to transfer to your<br>computer to use with your favourite<br>listening device</div>
  </div>
  <span class="folio left">2</span>
</section>

<section class="page p3">
  <div class="top"></div><div class="band"></div>
  <span class="running right">HYPNOSIS SESSION</span>
  <div class="abs h" style="left:17px;top:72px">HOW TO USE</div>
  <div class="abs small" style="left:17px;top:94px;width:222px">
    <p>The difference between the daytime and the bedtime version is the ending. There is no need to listen to both of these, the alternate endings have been provided for your convenience.</p>
    <p style="margin-top:4px">Many people like to listen before bedtime and the feedback has been that they do not wish to be awoken “feeling energised” if they are going to go to sleep after.</p>
    <p class="sub" style="margin-top:3px">Warning:</p>
    <p>Do not listen whilst driving or operating machinery.</p>
  </div>
  <p class="abs partner" style="left:20px;top:190px;width:212px">In partnership with <b>Northwind Airways</b>, Luke produced the first inflight hypnotherapy channel where a selection of his recordings have been made available on more than 30,000 flights worldwide.</p>
  <div class="cabin" role="img" aria-label="Photo of an aircraft cabin with seat-back screens showing the hypnotherapy channel"></div>
  <span class="folio right" style="color:#fff">3</span>
</section>

<!-- Spread: pages 4–5 -->
<section class="page p4 lilac-bg">
  <div class="top"></div><div class="band"></div>
  <span class="running left">HYPNOSIS SESSION</span>
  <svg class="wave" viewBox="0 0 70 311" preserveAspectRatio="none"><path d="M70 0 L50 0 C20 40 60 80 35 150 C15 210 50 270 45 311 L70 311Z" fill="#f4f4f7"/></svg>
  <div class="portrait" role="img" aria-label="Head-and-shoulders portrait of the hypnotherapist smiling"></div>
  <p class="abs small" style="left:17px;top:197px;width:125px;color:var(--muted)">Luke is a qualified and experienced Hypnotherapist who practices in Plymouth &amp; London. He is a member of the following professional governing bodies:</p>
  <div class="badge" style="left:17px;width:112px"><div class="fill" style="background:var(--navy)"></div></div>
  <div class="badge" style="left:135px;width:74px"><div class="fill" style="background:#3c9a6a"></div></div>
  <span class="folio left">4</span>
</section>

<section class="page p5">
  <div class="top"></div><div class="band"></div>
  <span class="running right">HYPNOSIS SESSION</span>
  <div class="abs h" style="left:25px;top:70px">ABOUT LUKE</div>
  <p class="abs small" style="left:25px;top:92px;width:200px">Luke is passionate about people and sees Hypnotherapy as the most effective tool for positively impacting on our hugely powerful brains. As well as ensuring that his techniques and practices are at the cutting edge of the latest developments into the brain, he also has a huge amount of life experience, including leading operations in highly stressful environments in his previous work with the Serious Offences Investigation Unit and the National Investigations Bureau.</p>
  <div class="abs sub" style="left:25px;top:210px">Experience &amp; Qualifications</div>
  <p class="abs small" style="left:49px;top:223px;width:178px">Luke is a fully qualified and insured Solution Focused Hypnotherapist. His products and services assist over 30,000 people every year and have reached more than 20 different countries. He is the producer of the first inflight Hypnotherapy channel in partnership with Northwind Airways. He has experience working with a wide variety of people including celebrities and high profile people. His client confidentiality is always of paramount importance.</p>
  <span class="folio right">5</span>
</section>

<!-- Spread: pages 6–7 -->
<section class="page p6">
  <div class="top"></div><div class="band"></div>
  <span class="running left">HYPNOSIS SESSION</span>
  <div class="abs h" style="left:16px;top:70px;font-size:13px">FREQUENTLY ASKED QUESTIONS</div>
  <div class="abs" style="left:16px;top:88px;width:222px">
    <p class="faq-q">Lorem ipsum dolor sit?</p>
    <p class="faq-a">integre ocurreret an sea, te ubique aperiri sanctus sit. Id cum nonumy concludaturque. Pro ne oblique constituam. Sed ne veniam graeco, est ex congue aperiam laboramus. Duo everti instructor ad.</p>
    <p class="faq-q">Lorem ipsum dolor sit amet, modo?</p>
    <p class="faq-a">integre ocurreret an sea, te ubique aperiri sanctus sit. Id cum nonumy concludaturque. Pro ne oblique constituam. Sed ne veniam graeco, est ex congue.</p>
    <p class="faq-q">Lorem ipsum dolor sit amet?</p>
    <p class="faq-a">integre ocurreret an sea, te ubique aperiri sanctus sit. Id cum nonumy concludaturque. Pro ne oblique constituam. Sed ne veniam graeco, est ex congue aperiam laboramus.</p>
    <p class="faq-q">Lorem ipsum dolor sit amet, modo?</p>
    <p class="faq-a">integre ocurreret an sea, te ubique aperiri sanctus sit. Id cum nonumy concludaturque. Pro ne oblique constituam. Sed ne veniam graeco, est ex congue.</p>
    <p class="faq-q">Lorem ipsum dolor sit amet?</p>
    <p class="faq-a">integre ocurreret an sea, te ubique aperiri sanctus sit. Id cum nonumy concludaturque. Pro ne oblique constituam.</p>
  </div>
  <span class="folio left">6</span>
</section>

<section class="page p7">
  <div class="top"></div><div class="band"></div>
  <span class="running right">HYPNOSIS SESSION</span>
  <div class="abs h" style="left:26px;top:62px;color:#fff;font-size:14px">EXCLUSIVE</div>
  <div class="deal"><span class="big">50% OFF</span><br>OF YOUR FIRST<br>DOWNLOAD</div>
  <p class="abs" style="left:41px;top:145px;width:190px;font-size:11.5px;font-weight:300;line-height:1.15;color:#fff">Go to the website, input the following code at checkout and get <b style="font-weight:800;font-size:14px">50% off</b></p>
  <p class="abs" style="left:68px;top:195px;font-size:10.5px;color:#fff">Code: <b style="font-weight:800;font-size:12px">exclusive50</b></p>
  <div class="brand abs" style="left:0;width:100%;top:243px"><span class="dot"></span><span class="name" style="font-size:14px">LUKE HARWOOD</span><span class="line2" style="font-size:14px">HYPNOTHERAPY</span></div>
  <div class="url abs" style="width:100%;text-align:center;top:322px">LukeHarwoodHypnotherapy.com</div>
  <span class="folio right" style="color:#fff">7</span>
</section>

<!-- Back cover -->
<section class="page back">
  <div class="top"></div><div class="band"></div>
  <div class="brand"><span class="dot"></span><span class="name">LUKE HARWOOD</span><span class="line2">HYPNOTHERAPY</span></div>
  <div class="url">LukeHarwoodHypnotherapy.com</div>
  <div class="photo" role="img" aria-label="Portrait of the hypnotherapist in a dark blazer, smiling"></div>
</section>

</body>
</html>
```